Flyer-Design für neues Produkt gesucht
Zielgruppe
Wir sind ein Adressbroker (Prima KONTAKT) und benötigen einen Flyer für unser neues Produkt Prima KONTAKT FLEX.
Zielgruppe sind Unternehmen, Werbeagenturen usw.
Weitere Infos können Sie gerne über unsere Webseite www.prima-kontakt-beispiel.de beziehen.
Aufgabenstellung
Wichtig ist uns eine übersichtliche Darstellung, vor allem der Vorteile.

```html
<!DOCTYPE html>
<html lang="de">
<head>
<meta charset="utf-8">
<title>Prima KONTAKT FLEX – Flyer</title>
<link href="https://fonts.googleapis.com/css2?family=Bebas+Neue&family=Open+Sans:wght@400&display=swap" rel="stylesheet">
<style>
  :root {
    --stage: #2f4361;
    --paper: #ededeb;
    --navy: #17304a;
    --navy-deep: #0f2236;
    --green: #7ab83a;
    --ink: #3f4246;
    --rule: #6d6f72;
    --white: #ffffff;
  }
  * { box-sizing: border-box; margin: 0; padding: 0; }
  html, body { width: 1200px; height: 800px; overflow: hidden; }
  body {
    background: var(--stage);
    display: flex; align-items: center; justify-content: center;
    font-family: "Bebas Neue", "Oswald", sans-serif;
  }
  .flyer {
    position: relative;
    width: 524px; height: 740px;
    background: var(--paper);
    overflow: hidden;
  }
  .flyer-shapes { position: absolute; inset: 0; }
  .brand {
    position: absolute; top: 30px; left: 188px;
    display: flex; align-items: center; gap: 10px;
    font-family: "Open Sans", sans-serif; font-size: 19px;
    color: var(--navy);
  }
  .brand-dot { width: 46px; height: 46px; border-radius: 50%; background: var(--green); }
  .headline {
    position: absolute; left: 62px; top: 150px;
    line-height: 0.86; text-transform: uppercase;
  }
  .headline-bracket {
    position: absolute; left: 32px; top: 160px;
    width: 40px; height: 178px;
    border-left: 6px solid var(--navy-deep);
    border-top: 6px solid var(--navy-deep);
  }
  .headline-line { display: block; }
  .headline-prima { color: var(--navy); font-size: 74px; padding-left: 60px; }
  .headline-kontakt { color: var(--green); font-size: 66px; padding-left: 26px; }
  .headline-flex { color: var(--green); font-size: 112px; }
  .benefits-title {
    position: absolute; left: 44px; top: 410px;
    color: var(--white); font-size: 27px; letter-spacing: 0.5px;
  }
  .duration {
    position: absolute; left: 336px; top: 440px;
    color: var(--white); font-size: 34px;
  }
  .benefits {
    position: absolute; left: 18px; right: 18px; top: 500px;
    display: grid; grid-template-columns: repeat(5, 1fr);
    row-gap: 26px;
  }
  .benefit {
    min-height: 52px;
    display: flex; align-items: center; justify-content: center;
    text-align: center; padding: 0 6px;
    font-size: 13.5px; line-height: 1.05; color: var(--ink);
    text-transform: uppercase;
    border-left: 4px solid var(--rule);
  }
  .benefit:nth-child(5n+1) { border-left: none; }
  .closing {
    position: absolute; left: 24px; right: 60px; top: 664px;
    color: var(--white); font-size: 17px; line-height: 1.05;
    text-align: center; text-transform: uppercase;
  }
</style>
</head>
<body>
  <main class="flyer">
    <svg class="flyer-shapes" width="524" height="740" viewBox="0 0 524 740">
      <defs>
        <linearGradient id="photoTone" x1="0" y1="0" x2="1" y2="1">
          <stop offset="0" stop-color="#1d3a5c"/>
          <stop offset="0.55" stop-color="#1a3f5e"/>
          <stop offset="1" stop-color="#0f2438"/>
        </linearGradient>
      </defs>
      <polygon class="hero-photo" role="img"
        aria-label="Foto: Geschäftsmann im Anzug hält ein Tablet, über dem ein leuchtendes Börsen-Kerzendiagramm schwebt"
        points="280,70 524,70 524,420 60,420" fill="url(#photoTone)"/>
      <polygon class="banner-title" points="18,398 380,398 380,458 18,458" fill="var(--navy)"/>
      <polygon class="banner-duration" points="336,430 486,430 486,484 296,484" fill="var(--green)"/>
      <rect class="band-closing" x="0" y="650" width="524" height="90" fill="var(--navy)"/>
      <polygon class="corner-accent" points="524,680 524,740 440,740" fill="var(--green)"/>
    </svg>

    <div class="brand">
      <span class="brand-name">Prima KONTAKT</span>
      <span class="brand-dot" aria-hidden="true"></span>
    </div>

    <div class="headline-bracket" aria-hidden="true"></div>
    <h1 class="headline">
      <span class="headline-line headline-prima">Prima</span>
      <span class="headline-line headline-kontakt">Kontakt</span>
      <span class="headline-line headline-flex">Flex</span>
    </h1>

    <h2 class="benefits-title">Vorteile Prima Kontakt Flex</h2>
    <p class="duration">12 Monate</p>

    <ul class="benefits">
      <li class="benefit">Zugang zu 4,2 Mio Firmendaten</li>
      <li class="benefit">1,4 Mio Entscheider-Daten</li>
      <li class="benefit">24 Stunden täglich, 7 Tage die Woche verfügbar</li>
      <li class="benefit">25.000 Datensätze monatlich exportierbar</li>
      <li class="benefit">Komfortabler Export als CSV-File</li>
      <li class="benefit">Einfache Bedienung</li>
      <li class="benefit">Keine Mindestmengen, egal ob 500 oder 5.000 Daten je Selektion</li>
      <li class="benefit">Flexible Selektions&shy;gestaltung</li>
      <li class="benefit">Firmendaten aus 3.600 Branchen wählen</li>
      <li class="benefit">Ständige Daten&shy;aktualisierung</li>
    </ul>

    <p class="closing">Bei voller Kostenkontrolle. Keine Datenzuschläge oder Selektionskosten.<br>Zahlung monatlich, viertel-, halbjährlich oder jährlich</p>
  </main>
</body>
</html>
```